Stonefield Partners Business Card Design

We are looking for a new business card design, we are not happy with our current design. We are a boutique management consulting firm and our clients are typically fortune 500 companies.

I have attached the current front and back that we have as well as a version of our logo that can be used. I am trying to get a higher resolution version of the logo file to upload to the project.

Target Market(s)

Fortune 500 companies are our primary client base. Financial services, life sciences, pharmaceuticals and telecom companies are

Industry/Entity Type

Management Consulting

Contact Information for Business Card

We are trying to communicate a high degree of professionalism, a somewhat minimalist perhaps with some air of whimsy (without overdoing it). Attached is the current design, front and back as well as logos. I like the current back of the card and assume we will keep the phrase the same.

From a color palette perspective, I prefer to stay with a gray scale as they are today.

Font styles to use
Sans Serif

Colors
1b1b1b
474747
ffffff

Requirements
Must have
• Two sided business card design. File format should be something that can be used outside of Photoshop like MS Publisher so that they can be edited with personal information.
• Font should be calibri or something very similar and should be available within MS Office
Should not have
• No other logos or graphics outside of the logo provided.

```html
<!DOCTYPE html>
<html lang="en">
<head>
<meta charset="utf-8">
<title>Stonefield Partners Business Card</title>
<link rel="stylesheet" href="https://fonts.googleapis.com/css2?family=Carlito:wght@400;700&display=swap">
<style>
  :root {
    --stage: #2b2b2b;
    --ink: #1b1b1b;
    --black: #000000;
    --mid: #474747;
    --white: #ffffff;
    --grey-light: #d4d4d4;
    --grey-dark: #8c8c8c;
  }
  * { margin: 0; padding: 0; box-sizing: border-box; }
  html, body {
    width: 1022px; height: 1200px; overflow: hidden;
    background: var(--stage);
    font-family: "Carlito", "Calibri", sans-serif;
  }
  .card {
    position: absolute; left: 93px; width: 833px; height: 513px; overflow: hidden;
  }
  .card--front { top: 64px; }
  .card--back {
    top: 615px;
    background: linear-gradient(to bottom, var(--grey-light), #b4b4b4 55%, var(--grey-dark));
  }
  .card__bg { position: absolute; inset: 0; width: 100%; height: 100%; }
  .brand {
    position: absolute; left: 147px; top: 46px;
    display: flex; align-items: center; gap: 16px;
    color: var(--white); font-weight: 700; font-size: 82px; line-height: 1;
  }
  .brand__dot { width: 62px; height: 62px; border-radius: 50%; background: var(--white); }
  .contact {
    position: absolute; font-size: 21px; line-height: 30px; color: var(--ink);
  }
  .contact strong { font-weight: 700; }
  .contact--person { left: 63px; top: 314px; }
  .contact--office { left: 510px; top: 310px; }
  .divider { position: absolute; left: 426px; top: 288px; width: 14px; height: 172px; }
  .tagline {
    position: absolute; left: 0; right: 0; top: 140px; text-align: center;
    font-weight: 700; font-size: 37px; line-height: 48px; color: var(--black);
    padding-left: 28px;
  }
  .rule { position: absolute; left: 42px; top: 386px; width: 780px; height: 14px; }
  .website {
    position: absolute; left: 0; right: 0; top: 441px; text-align: center;
    font-weight: 700; font-size: 21px; color: var(--ink);
  }
</style>
</head>
<body>
  <section class="card card--front">
    <svg class="card__bg" viewBox="0 0 833 513" preserveAspectRatio="none" aria-hidden="true">
      <defs>
        <linearGradient id="frontGrey" x1="0" y1="0" x2="0" y2="1">
          <stop offset="0" stop-color="#c9c9c9"/>
          <stop offset="1" stop-color="#8a8a8a"/>
        </linearGradient>
      </defs>
      <rect width="833" height="513" fill="url(#frontGrey)"/>
      <path d="M0,0 H833 V283 C760,240 690,228 560,228 C380,228 200,190 0,128 Z" fill="var(--black)"/>
      <g fill="none" stroke="var(--white)">
        <path d="M0,140 C200,205 380,240 560,240 C690,240 760,250 833,292" stroke-width="4"/>
        <path d="M0,150 C180,205 330,230 470,238" stroke-width="2" opacity="0.8"/>
        <path d="M0,160 C160,207 300,228 420,236" stroke-width="2" opacity="0.7"/>
        <path d="M0,172 C140,210 260,228 370,234" stroke-width="1.5" opacity="0.6"/>
      </g>
    </svg>
    <div class="brand"><span class="brand__dot"></span><span>Stonefield</span></div>
    <div class="contact contact--person">
      <strong>Dana Whitfield</strong><br>
      Los Angeles Office<br>
      Managing Director<br>
      206.555.0142<br>
      dwhitfield@stonefieldpartners.com
    </div>
    <svg class="divider" viewBox="0 0 14 172" aria-hidden="true">
      <path d="M7,0 C10,60 10,112 7,172 C4,112 4,60 7,0 Z" fill="var(--black)"/>
    </svg>
    <div class="contact contact--office">
      <strong>Stonefield Partners, Inc.</strong><br>
      Headquarters<br>
      218 Harbor Lane<br>
      Suite 210<br>
      Cedar Point, WA 98000
    </div>
  </section>

  <section class="card card--back">
    <p class="tagline">The preferred choice<br>for leadership’s top priorities</p>
    <svg class="rule" viewBox="0 0 780 14" preserveAspectRatio="none" aria-hidden="true">
      <path d="M0,7 C200,3 580,3 780,7 C580,11 200,11 0,7 Z" fill="var(--white)"/>
    </svg>
    <p class="website">www.StonefieldPartners.com</p>
  </section>
</body>
</html>
```